Präsentationsvorlagen für Immobilienvertrieb
Zielgruppe
Wir sind ein Immobilienvertrieb im Bereich Neubau- und Bestandsimmobilien aus München. Die Firma BRIX existiert seit über 30 Jahren. Vor 5 Jahren haben wir ein cooles modernes Rebranding durchgeführt, sodass man mit unserem neuen Corporate Design richtig Spaß am Gestalten haben kann.
Eine konkrete Zielgruppe zu definieren ist schwierig, da unsere Käufer von 20-80 Jahren sein können. Ob junge, erfolgreiche Menschen, junge Familien, ältere Erwachsene, die von sich nach Auszug ihrer Kinder von ihrem Haus trennen wollen und eine kleinere Wohnung suchen oder einfach der Kapitalanleger, der auf der Suche nach einer neuen Investition ist.
Unsere CI ist gradlinig und setzt sich aus anthrazit, neonorange und weiß zusammen.
Im Bestand gibt es nicht pro Objekt ein CI, hier wird mit dem der BRIX gearbeitet.
Im Neubau hat jedes einzelne Projekt sein eigenes CI (siehe aktuell wohnfeld-plus.de).
www.brix-wohnen.de
Aufgabenstellung
Zur Aufgabe: Für sowohl interne als auch externe Präsentationen benötigen wir eine firmeneinheitliche PowerPoint-Präsentationsvorlage, die sich wandelbar und modern von 'normalen' Präsentationen abhebt.
Vorgaben:
- CI der BRIX muss verwendet werden (CI-Styleguide anbei)
- ansonsten sind der Kreativität keine Grenzen gesetzt
Die derzeitige Vorlage ist anbei.

```html
<!DOCTYPE html>
<html lang="de">
<head>
<meta charset="utf-8">
<title>BRIX – Präsentationsvorlage</title>
<link href="https://fonts.googleapis.com/css2?family=Jost:wght@300;400;500;600;700&display=swap" rel="stylesheet">
<style>
:root{
  --page:#eeeeee;
  --anthracite:#2b2b2b;
  --anthracite-deep:#1f1f1f;
  --orange:#fa4616;
  --beige:#d3c3a5;
  --white:#ffffff;
  --muted:#8a8a8a;
  --dim:#555555;
}
*{margin:0;padding:0;box-sizing:border-box}
html,body{width:1200px;height:1089px;overflow:hidden;background:var(--page);font-family:'Jost',sans-serif;color:var(--white)}
.canvas{position:relative;width:1200px;height:1089px}
.slide{position:absolute;width:555px;height:313px;background:var(--anthracite);overflow:hidden}
.abs{position:absolute}
.accent-bar{position:absolute;right:0;top:0;width:6px;height:100%;background:var(--orange)}
.brand{position:absolute;left:13px;top:18px;font-weight:600;font-size:11px;letter-spacing:1px;color:var(--white)}
.rail{position:absolute;left:24px;top:48px;width:1px;height:170px;background:var(--dim)}
.pager{position:absolute;left:20px;top:234px;font-size:4px;line-height:15px;color:var(--dim)}
.pager .on{color:var(--white);font-size:6px}
.badge{position:absolute;width:26px;height:26px;border:1px dashed var(--orange);border-radius:50%}
.eyebrow{position:absolute;font-weight:300;font-size:16px;color:var(--white)}
.eyebrow-line{position:absolute;height:1px;background:var(--orange)}
.headline{position:absolute;font-weight:700;font-size:25px;line-height:1;letter-spacing:.5px}
.headline .dot{color:var(--orange)}
.headline .soft{font-size:20px;font-weight:600}
.lead{position:absolute;font-size:6.5px;font-weight:600}
.lead::before{content:"";position:absolute;left:-18px;top:1px;border-left:4px solid var(--orange);border-top:3px solid transparent;border-bottom:3px solid transparent}
.body{position:absolute;font-size:5.6px;line-height:9.6px;color:#d8d8d8;text-align:justify}
.photo{position:absolute}
.outline-btn{position:absolute;border:1px solid var(--orange);font-size:5px;font-weight:600;letter-spacing:.8px;display:flex;align-items:center;justify-content:center}
/* cover */
.cover .photo{inset:0;background:linear-gradient(160deg,#3a3936 0%,#2c2b28 40%,#3b342c 70%,#1e1e1d 100%)}
.cover .shade{position:absolute;inset:0;background:rgba(25,25,25,.55)}
.cover .brand{left:51px;top:56px;font-size:20px;letter-spacing:2px}
.cover .kicker{left:50px;top:123px;font-weight:300;font-size:27px;color:var(--orange);letter-spacing:.5px}
.cover .title{left:50px;top:159px;font-weight:700;font-size:31px;letter-spacing:.5px}
.cover .sub{left:51px;top:198px;font-size:6.5px;font-weight:500}
.cover .year{left:437px;top:20px;width:60px;height:190px}
/* contents */
.toc-item{position:absolute;width:130px}
.toc-num{font-size:18px;font-weight:600;color:var(--orange);line-height:1}
.toc-bar{width:21px;height:2px;background:var(--beige);margin-top:4px}
.toc-title{position:absolute;left:30px;top:8px;font-size:6.5px;font-weight:600;line-height:8px}
.toc-text{font-size:5.5px;line-height:8px;color:#cfcfcf;margin-top:9px;width:95px}
/* buttons */
.btn-orange{position:absolute;background:var(--orange);display:flex;align-items:center}
.btn-beige{position:absolute;background:var(--beige);display:flex;align-items:center;justify-content:center}
/* services */
.svc-icon{position:absolute;width:21px;height:21px;display:flex;align-items:center;justify-content:center}
.svc-name{position:absolute;font-size:6.5px;font-weight:700}
.svc-text{position:absolute;font-size:5.6px;line-height:7.5px;color:#d8d8d8;width:98px}
.svc-arrow{position:absolute;width:24px;height:6px}
/* contact */
.label{position:absolute;font-size:7px;font-weight:600;letter-spacing:.8px;color:var(--orange)}
.info{position:absolute;font-size:5.8px;line-height:10px;color:#e6e6e6}
</style>
</head>
<body>
<div class="canvas">

  <!-- Cover -->
  <section class="slide cover" style="left:34px;top:42px">
    <div class="photo" role="img" aria-label="Luftaufnahme einer Münchner Prachtstraße mit Triumphbogen in der Dämmerung"></div>
    <div class="shade"></div>
    <div class="brand abs">BRIX</div>
    <div class="abs kicker">BUSINESS</div>
    <div class="abs title">PRESENTATION</div>
    <div class="abs sub">Lorem ipsum is simply dummy text of the printing and typesetting industry.</div>
    <div class="outline-btn" style="left:51px;top:242px;width:79px;height:18px">TEXT TITTLE HERE</div>
    <svg class="abs year" viewBox="0 0 60 190"><text x="30" y="95" transform="rotate(-90 30 95)" text-anchor="middle" dominant-baseline="middle" font-family="Jost, sans-serif" font-size="56" font-weight="300" fill="none" stroke="#6a6a6a" stroke-width="1">2023</text></svg>
    <div class="abs" style="left:503px;top:17px;width:1px;height:190px;background:var(--orange)"></div>
    <div class="abs" style="left:260px;top:259px;width:186px;height:1px;background:var(--orange)"></div>
    <div class="badge" style="left:466px;top:224px;width:72px;height:72px"></div>
  </section>

  <!-- Table of content -->
  <section class="slide" style="left:612px;top:42px">
    <div class="brand">BRIX</div>
    <div class="rail"></div>
    <div class="pager"><div class="on">02</div><div>03</div><div>04</div><div>05</div><div>06</div></div>
    <div class="eyebrow" style="left:70px;top:48px">Table Of</div>
    <div class="eyebrow-line" style="left:147px;top:58px;width:81px"></div>
    <div class="headline" style="left:70px;top:72px">CONTENT<span class="dot">.</span></div>
    <p class="body" style="left:277px;top:76px;width:190px;text-align:left">Lorem ipsum dolor sit amet, consetetur sadipscing elitr, sed diam nonumy eirmod tempor invidunt ut labore et dolore magna.</p>
    <div class="toc-item" style="left:72px;top:130px"><div class="toc-num">01</div><div class="toc-bar"></div><div class="toc-title">ONE CONTENT<br>TITLE TEXT HERE</div><p class="toc-text">Lorem ipsum dolor sit amet, duis at consetetur sadipscing.</p></div>
    <div class="toc-item" style="left:218px;top:130px"><div class="toc-num">02</div><div class="toc-bar"></div><div class="toc-title">TWO CONTENT<br>TITLE TEXT HERE</div><p class="toc-text">Lorem ipsum dolor sit amet, duis at consetetur sadipscing.</p></div>
    <div class="toc-item" style="left:364px;top:130px"><div class="toc-num">03</div><div class="toc-bar"></div><div class="toc-title">THREE CONTENT<br>TITLE TEXT HERE</div><p class="toc-text">Lorem ipsum dolor sit amet, duis at consetetur sadipscing.</p></div>
    <div class="toc-item" style="left:72px;top:215px"><div class="toc-num">04</div><div class="toc-bar"></div><div class="toc-title">FOUR CONTENT<br>TITLE TEXT HERE</div><p class="toc-text">Lorem ipsum dolor sit amet, duis at consetetur sadipscing.</p></div>
    <div class="toc-item" style="left:218px;top:215px"><div class="toc-num">05</div><div class="toc-bar"></div><div class="toc-title">FIVE CONTENT<br>TITLE TEXT HERE</div><p class="toc-text">Lorem ipsum dolor sit amet, duis at consetetur sadipscing.</p></div>
    <div class="toc-item" style="left:364px;top:215px"><div class="toc-num">06</div><div class="toc-bar"></div><div class="toc-title">SIX CONTENT<br>TITLE TEXT HERE</div><p class="toc-text">Lorem ipsum dolor sit amet, duis at consetetur sadipscing.</p></div>
    <div class="badge" style="left:512px;top:270px"></div>
    <div class="accent-bar"></div>
  </section>

  <!-- Welcome -->
  <section class="slide" style="left:34px;top:389px">
    <div class="brand">BRIX</div>
    <div class="rail"></div>
    <div class="pager" style="top:234px"><div>02</div><div class="on">03</div><div>04</div><div>05</div><div>06</div></div>
    <div class="eyebrow" style="left:70px;top:48px">Welcome to</div>
    <div class="eyebrow-line" style="left:172px;top:58px;width:56px"></div>
    <div class="headline" style="left:70px;top:72px">BRIX <span class="soft">Company</span><span class="dot">.</span></div>
    <div class="lead" style="left:88px;top:110px">Lorem ipsum dolor sit amet</div>
    <p class="body" style="left:88px;top:135px;width:182px">Lorem ipsum dolor sit amet, consectetur adipiscing elit, sed do eiusmod tempor incididunt ut labore et dolore magna aliqua. Ut enim ad minim veniam, quis nostrud exercitation ullamco laboris nisi ut aliquip ex ea commodo consequat. Duis aute irure dolor in reprehenderit in voluptate velit esse cillum dolore eu fugiat nulla pariatur.</p>
    <svg class="abs" style="left:88px;top:212px" width="22" height="18" viewBox="0 0 22 18"><path d="M0 18V10C0 4 3 1 8 0v4C5 5 4 7 4 9h4v9zM12 18V10c0-6 3-9 8-10v4c-3 1-4 3-4 5h4v9z" fill="#3a3a3a"/></svg>
    <svg class="abs" style="left:260px;top:196px" width="22" height="18" viewBox="0 0 22 18"><path d="M22 0v8c0 6-3 9-8 10v-4c3-1 4-3 4-5h-4V0zM10 0v8c0 6-3 9-8 10v-4c3-1 4-3 4-5H2V0z" fill="#3a3a3a"/></svg>
    <p class="abs" style="left:122px;top:205px;font-size:9px;font-weight:300;line-height:11px;color:var(--orange)">Duis aute irure reprehendert<br>voluptate velit esse cillum</p>
    <div class="abs" style="left:91px;top:245px;font-size:9px;font-weight:300">+</div>
    <div class="abs" style="left:112px;top:247px;font-size:7px;font-weight:500;line-height:9px">LENA BRANDT<br><span style="font-size:5.8px;font-weight:400">Chief Executive Officer</span></div>
    <div class="photo" style="left:320px;top:0;width:229px;height:313px;background:linear-gradient(180deg,#8f9696 0%,#7b6f68 40%,#7d4a3a 60%,#6b6560 100%)" role="img" aria-label="Blick über die Münchner Altstadt mit Frauenkirche und Rathausturm"></div>
    <div class="btn-orange" style="left:263px;top:238px;width:57px;height:38px;justify-content:center">
      <svg width="24" height="6" viewBox="0 0 24 6"><path d="M24 3H1M4 0 1 3l3 3" stroke="#fff" stroke-width=".8" fill="none"/></svg>
    </div>
    <div class="btn-beige" style="left:320px;top:238px;width:32px;height:38px">
      <svg width="8" height="12" viewBox="0 0 8 12"><path d="M1 0l6 6-6 6" stroke="#fff" stroke-width=".8" fill="none"/></svg>
    </div>
    <div class="badge" style="left:512px;top:270px"></div>
    <div class="accent-bar"></div>
  </section>

  <!-- About -->
  <section class="slide" style="left:612px;top:389px">
    <div class="brand">BRIX</div>
    <div class="rail"></div>
    <div class="pager" style="top:234px"><div>02</div><div>03</div><div class="on">04</div><div>05</div><div>06</div></div>
    <div class="photo" style="left:70px;top:50px;width:183px;height:187px;background:linear-gradient(180deg,#d9d9d6 0%,#bdbcb8 45%,#242424 46%,#1c1c1c 85%,#6e4a32 100%)" role="img" aria-label="Empfangstresen im Büro mit Firmenschild an der Wand"></div>
    <div class="btn-orange" style="left:70px;top:237px;width:128px;height:38px;padding-left:14px;font-size:7px;font-weight:500;gap:14px"><span>+</span><span>LOREM IPSUM TEXT</span></div>
    <div class="btn-beige" style="left:198px;top:237px;width:55px;height:38px">
      <svg width="24" height="6" viewBox="0 0 24 6"><path d="M0 3h23M20 0l3 3-3 3" stroke="#fff" stroke-width=".8" fill="none"/></svg>
    </div>
    <div class="eyebrow" style="left:286px;top:48px">About</div>
    <div class="eyebrow-line" style="left:349px;top:58px;width:95px"></div>
    <div class="headline" style="left:286px;top:72px">BRIX <span class="soft">Company</span><span class="dot">.</span></div>
    <div class="lead" style="left:304px;top:110px">Lorem ipsum dolor sit amet</div>
    <p class="body" style="left:304px;top:131px;width:183px">Lorem ipsum dolor sit amet, consectetur adipiscing elit, sed do eiusmod tempor incididunt ut labore et dolore magna aliqua. Ut enim ad minim veniam, quis nostrud exercitation ullamco laboris nisi ut aliquip ex ea commodo consequat. Duis aute irure dolor in reprehenderit in voluptate velit esse cillum dolore eu fugiat nulla pariatur. Excepteur sint occaecat cupidatat non proident, sunt in culpa qui officia deserunt mollit anim id est laborum.</p>
    <p class="body" style="left:304px;top:207px;width:183px">Sed ut perspiciatis unde omnis iste natus error sit voluptatem accusantium doloremque laudantium, totam rem aperiam, eaque ipsa quae ab illo inventore veritatis et quasi architecto beatae vitae dicta sunt explicabo. Nemo enim ipsam voluptatem quia voluptas sit aspernatur aut odit aut fugit, sed quia consequuntur magni dolores eos qui ratione voluptatem sequi nesciunt. Neque porro quisquam est.</p>
    <div class="badge" style="left:512px;top:270px"></div>
    <div class="accent-bar"></div>
  </section>

  <!-- Service -->
  <section class="slide" style="left:34px;top:735px">
    <div class="brand">BRIX</div>
    <div class="rail"></div>
    <div class="pager" style="top:228px"><div>02</div><div>03</div><div>04</div><div class="on">05</div><div>06</div></div>
    <div class="eyebrow" style="left:70px;top:47px">Our</div>
    <div class="eyebrow-line" style="left:133px;top:58px;width:95px"></div>
    <div class="headline" style="left:70px;top:72px">SERVICE<span class="dot">.</span></div>
    <div class="lead" style="left:88px;top:110px">Lorem ipsum dolor sit amet</div>
    <p class="body" style="left:88px;top:135px;width:121px">Lorem ipsum dolor sit amet, consectetur adipiscing elit, sed do eiusmod tempor incididunt ut labore et dolore magna aliqua. Ut enim ad minim veniam, quis nostrud exercitation do ullamco laboris esse tempor cillum nisi ut aliquip ex dolore ea commodo consequat. Sed ut perspiciatis unde omnis iste natus voluptatem.</p>
    <div class="abs" style="left:88px;top:226px;font-size:6.5px;display:flex;align-items:center;gap:10px">2018<span style="width:25px;height:1px;background:#ccc"></span>2023</div>
    <div class="outline-btn" style="left:88px;top:259px;width:80px;height:17px">TEXT TITTLE HERE</div>

    <div class="svc-icon" style="left:260px;top:76px;background:var(--orange)"><svg width="11" height="11" viewBox="0 0 12 12"><circle cx="6" cy="6" r="5" stroke="#fff" fill="none"/><path d="M1 6h10M6 1c-3 3-3 7 0 10M6 1c3 3 3 7 0 10" stroke="#fff" fill="none" stroke-width=".7"/></svg></div>
    <div class="svc-name" style="left:290px;top:83px">SERVICE 01</div>
    <p class="svc-text" style="left:260px;top:111px">Lorem ipsum dolor sit amet, sed ut consectetur adipisicing elit, sed do eiusmod unde tempor incididunt ut labore et dolore magna aliqua.</p>
    <svg class="svc-arrow" style="left:260px;top:152px" viewBox="0 0 24 6"><path d="M0 3h23M20 0l3 3-3 3" stroke="#8a8a8a" stroke-width=".8" fill="none"/></svg>

    <div class="svc-icon" style="left:391px;top:76px;background:#8f8a82"><svg width="10" height="11" viewBox="0 0 10 11"><rect x="1" y="1" width="8" height="10" fill="none" stroke="#fff"/><path d="M3 3h1M6 3h1M3 5h1M6 5h1M4 11V8h2v3" stroke="#fff" fill="none" stroke-width=".8"/></svg></div>
    <div class="svc-name" style="left:423px;top:83px">SERVICE 02</div>
    <p class="svc-text" style="left:391px;top:111px">Lorem ipsum dolor sit amet, sed ut consectetur adipisicing elit, sed do eiusmod unde tempor incididunt ut labore et dolore magna aliqua.</p>
    <svg class="svc-arrow" style="left:391px;top:152px" viewBox="0 0 24 6"><path d="M0 3h23M20 0l3 3-3 3" stroke="#8a8a8a" stroke-width=".8" fill="none"/></svg>

    <div class="svc-icon" style="left:260px;top:196px;background:var(--beige)"><svg width="10" height="11" viewBox="0 0 10 11"><path d="M5 1 1 2.5V6c0 2.5 2 4 4 4.5 2-.5 4-2 4-4.5V2.5z" fill="none" stroke="#fff"/><path d="M3 6l1.5 1.5L7 5" stroke="#fff" fill="none" stroke-width=".8"/></svg></div>
    <div class="svc-name" style="left:290px;top:203px">SERVICE 03</div>
    <p class="svc-text" style="left:260px;top:228px">Lorem ipsum dolor sit amet, sed ut consectetur adipisicing elit, sed do eiusmod unde tempor incididunt ut labore et dolore magna aliqua.</p>
    <svg class="svc-arrow" style="left:260px;top:270px" viewBox="0 0 24 6"><path d="M0 3h23M20 0l3 3-3 3" stroke="#8a8a8a" stroke-width=".8" fill="none"/></svg>

    <div class="svc-icon" style="left:391px;top:196px;background:#6b4a40"><svg width="12" height="10" viewBox="0 0 12 10"><circle cx="3.5" cy="3" r="1.6" fill="none" stroke="#fff" stroke-width=".8"/><circle cx="8.5" cy="3" r="1.6" fill="none" stroke="#fff" stroke-width=".8"/><path d="M0.5 9c0-2 1.3-3 3-3s3 1 3 3M5.5 9c0-2 1.3-3 3-3s3 1 3 3" stroke="#fff" fill="none" stroke-width=".8"/></svg></div>
    <div class="svc-name" style="left:417px;top:203px">SERVICE 04</div>
    <p class="svc-text" style="left:391px;top:228px">Lorem ipsum dolor sit amet, sed ut consectetur adipisicing elit, sed do eiusmod unde tempor incididunt ut labore et dolore magna aliqua.</p>
    <svg class="svc-arrow" style="left:391px;top:270px" viewBox="0 0 24 6"><path d="M0 3h23M20 0l3 3-3 3" stroke="#8a8a8a" stroke-width=".8" fill="none"/></svg>

    <div class="badge" style="left:512px;top:270px"></div>
    <div class="accent-bar"></div>
  </section>

  <!-- Contact -->
  <section class="slide" style="left:612px;top:735px">
    <div class="brand">BRIX</div>
    <div class="rail"></div>
    <div class="headline" style="left:68px;top:58px;font-weight:600">Contact us<span class="dot">.</span></div>
    <div class="eyebrow-line" style="left:220px;top:77px;width:74px"></div>
    <div class="label" style="left:70px;top:109px">OFFICE HOURS</div>
    <div class="info" style="left:70px;top:120px">Monday - Saturday<br>09.00 - 18.00</div>
    <div class="label" style="left:170px;top:109px">GET IN TOUCH</div>
    <div class="info" style="left:172px;top:120px">+49 89 55 210-300</div>
    <div class="label" style="left:70px;top:155px">FOLLOW US</div>
    <div class="info" style="left:70px;top:166px">www.brix-wohnen.de<br>kontakt@brix-wohnen.de</div>
    <div class="label" style="left:173px;top:155px">OUR ADDRESS</div>
    <div class="info" style="left:171px;top:166px;line-height:8.5px">BRIX Immobilien GmbH<br>Lindenweg 12<br>80331 München</div>
    <div class="photo" style="left:293px;top:28px;width:235px;height:257px;background:linear-gradient(180deg,#a9b3bb 0%,#9e8f80 25%,#6f6a5f 55%,#3d3a35 100%)" role="img" aria-label="Luftbild einer Münchner Allee mit Triumphbogen und Stadtsilhouette"></div>
    <div class="abs" style="left:293px;top:220px;width:235px;height:65px;background:linear-gradient(180deg,rgba(30,30,30,0),rgba(30,30,30,.7))"></div>
    <p class="abs" style="left:325px;top:232px;width:182px;font-size:5.6px;line-height:8.5px">Lorem ipsum dolor sit amet, consectetur adipiscing elit, sed do eiusmod tempor incididunt ut labore et dolore magna aliqua. Ut enim ad minim veniam, quis nostrud exercitation ullamco laboris esse cillum nisi ut aliquip ex ea commodo consequat.</p>
    <div class="abs" style="left:66px;top:217px;width:24px;height:68px;background:var(--beige)"></div>
    <div class="btn-orange" style="left:90px;top:217px;width:203px;height:68px">
      <svg class="abs" style="left:24px;top:31px" width="34" height="6" viewBox="0 0 34 6"><path d="M0 3h33M30 0l3 3-3 3" stroke="#fff" stroke-width=".8" fill="none"/></svg>
      <p class="abs" style="left:82px;top:14px;font-size:11px;line-height:14px;font-weight:500">Dui lorem duis<br>Sit amet<br>Doloris in ciu.</p>
    </div>
    <div class="badge" style="left:11px;top:270px"></div>
  </section>

</div>
</body>
</html>
```